■依頼の目的/概要
電子書籍の魅力的な表紙デザインをお願いします。

デザインのテイストについてはお任せします!
できるだけたくさんの方の目にとまるよう、スマホで見ても文字が読みやすければいいかと思います。

■本の内容
専門書ではなく、コーヒーのある暮らしと、楽しみ方を提案する本です。
現役バリスタであり、コーヒー教室の先生である「森っち先生(30代男性)」に、生徒の主婦が色々と質問をする、軽妙な対談形式になっています。

■読者ターゲット
コーヒーを愛する方、コーヒーに興味がある方

【表紙に入れて頂きたい項目】
■タイトル
SLOW DRIP, SLOW DAYS
毎日を少し豊かにする習慣
バリスタ森っち先生とコーヒー実践対談

■著者
コーヒーライフクリエーター柴田美穂
<監修>
K.B.R.T.認定コーヒーインストラクター1級
バリスタ森っち先生

■読者プレゼント
カップの選び方で見える心の傾向

【添付資料】
①著作内容のワードファイルをつけましたのでご一読ください。

②森っち先生の写真
本人の画像です。
お任せしますが、全面でなく小さめに使って頂いたらいいかと思います。
30代男性バリスタのイラストでも結構です。

※白樺堂MP奈良店の現役バリスタです。
写真はホームページのブログ、2019/12/3 K.B.R.Tコーヒーインストラクター
1級取得のページに掲載されているものです。
もし添付画像が開かなければ、お手数ですがそちらから取ってください。

その他何かご不明な点がございましたら、お気軽にご質問下さい。
では楽しみにしています。よろしくお願いいたします!

①タイトル SLOW DRIP, SLOW DAYSが、メインタイトルとして表現されているか
②コーヒーの香りや味わいが表現されているか
③若い層や女性に関心をもってもらえる表現かどうか
コーヒー愛好家の中心層は中高年男性です。本著は30代以下の若年層や女性にも
ファンを広げるために、美容・アレンジメニューなどの情報も書きました。
そこで今回は、調査で若年層が好きだと選んだ案を採用させて頂きました。
特に決定案は、コーヒーの香りを楽しんでいるような瞑想風のイラストが秀逸でした。

今回ご参加下さったすべてのランサー様に厚く御礼申し上げます。
書籍を読んでくださった方、複数案を製作下さった方、クリエーターとしてのキャリアを感じる素晴らしいデザイン、コーヒーの専門書にふさわしい風格あるデザイン、雑誌のような夢のあるデザイン、今どきの若者らしいデザイン。 採用案以外にも、ああこれいいなあ・・というものがたくさんありました。重ねて皆様に感謝いたします。皆様のご活躍を祈念しております。

```html
<!DOCTYPE html>
<html lang="ja">
<head>
<meta charset="utf-8">
<title>SLOW DRIP, SLOW DAYS</title>
<link rel="stylesheet" href="https://fonts.googleapis.com/css2?family=Zilla+Slab:wght@700&family=M+PLUS+Rounded+1c:wght@700;800&family=Noto+Sans+JP:wght@500;700;900&display=swap">
<style>
  :root{
    --paper:#efe2cc;
    --paper-deep:#e5d3b5;
    --ink:#4a3022;
    --accent:#e07f2a;
    --band:#4b2f20;
    --white:#fffaf2;
    --yellow:#f6c445;
    --pink:#e7566a;
  }
  *{margin:0;padding:0;box-sizing:border-box}
  html,body{width:750px;height:1200px;overflow:hidden;background:var(--paper)}
  .cover{position:relative;width:750px;height:1200px;overflow:hidden;
    background:radial-gradient(ellipse at 40% 30%,var(--paper) 0%,var(--paper-deep) 100%);
    font-family:"Noto Sans JP",sans-serif;color:var(--ink)}
  .title{position:absolute;left:44px;top:40px;font-family:"Zilla Slab",serif;font-weight:700;
    font-size:128px;line-height:118px;letter-spacing:2px;color:var(--ink)}
  .cup-art{position:absolute;left:545px;top:36px;width:185px;height:140px;border-radius:50%;
    background:radial-gradient(circle,#c9a27a 0%,rgba(229,211,181,0) 72%)}
  .scene-art{position:absolute;left:480px;top:290px;width:255px;height:370px;border-radius:45% 45% 18% 18%;
    background:linear-gradient(160deg,#f2b9a2 0%,#d9a57a 55%,#b07b55 100%);opacity:.85}
  .gift{position:absolute;left:470px;top:130px;width:210px;height:150px;z-index:2}
  .gift-flag{position:absolute;left:85px;top:0;background:var(--pink);color:var(--white);white-space:nowrap;
    font:700 18px/1 "Noto Sans JP",sans-serif;padding:7px 10px;transform:rotate(-6deg);z-index:3}
  .gift-badge{position:absolute;left:0;top:44px;width:200px;height:104px;border-radius:50%;
    background:var(--white);display:flex;flex-direction:column;align-items:center;justify-content:center;
    font:700 19px/1.35 "M PLUS Rounded 1c",sans-serif;color:var(--ink);text-align:center}
  .gift-badge .em{color:var(--pink);font-size:21px}
  .author{position:absolute;left:44px;top:560px}
  .author-role{font:700 24px/1 "Noto Sans JP",sans-serif;color:var(--ink)}
  .author-name{margin-top:14px;font:900 56px/1 "Noto Sans JP",sans-serif;color:var(--ink);letter-spacing:4px}
  .author-name small{font-size:28px;letter-spacing:0;margin-left:6px}
  .subtitle{position:absolute;left:0;width:750px;top:820px;text-align:center;white-space:nowrap;
    font:900 50px/1 "M PLUS Rounded 1c",sans-serif;color:var(--ink);letter-spacing:1px}
  .subtitle .em{color:var(--accent);font-size:62px}
  .band{position:absolute;left:0;top:925px;width:750px;height:275px;background:var(--band)}
  .band-lead{position:absolute;left:72px;top:40px;font:900 44px/1 "Noto Sans JP",sans-serif;color:var(--white);white-space:nowrap}
  .band-title{position:absolute;left:70px;top:108px;font:900 60px/1 "Noto Sans JP",sans-serif;color:var(--yellow);letter-spacing:1px;white-space:nowrap}
  .supervision{position:absolute;left:70px;top:192px;display:flex;align-items:center;gap:14px}
  .supervision-tag{background:var(--white);color:var(--band);font:900 24px/1.05 "Noto Sans JP",sans-serif;
    padding:8px 6px;border-radius:6px;width:42px;text-align:center}
  .supervision-role{font:700 19px/1 "Noto Sans JP",sans-serif;color:var(--white);white-space:nowrap}
  .supervision-name{margin-top:8px;font:900 42px/1 "Noto Sans JP",sans-serif;color:var(--white);white-space:nowrap}
  .portrait{position:absolute;left:580px;top:25px;width:140px;height:250px;border-radius:65px 65px 8px 8px;
    background:linear-gradient(180deg,#6b4a36 0%,#2f2019 100%)}
</style>
</head>
<body>
<main class="cover">
  <div class="cup-art" role="img" aria-label="湯気の立つコーヒーカップとコーヒー豆の袋のイラスト"></div>
  <h1 class="title">SLOW<br>DRIP,<br>SLOW<br>DAYS</h1>
  <div class="scene-art" role="img" aria-label="椅子に座り目を閉じてコーヒーの香りを楽しむ女性とドリップ器具のイラスト"></div>
  <div class="gift">
    <div class="gift-badge"><span>カップの選び方で</span><span class="em">見える心の傾向</span></div>
    <div class="gift-flag">読者プレゼント</div>
  </div>
  <div class="author">
    <p class="author-role">コーヒーライフクリエーター</p>
    <p class="author-name">柴田美穂<small>[著]</small></p>
  </div>
  <p class="subtitle">毎日を<span class="em">少し</span>豊かにする習慣</p>
  <section class="band">
    <p class="band-lead">バリスタ森っち先生と</p>
    <p class="band-title">コーヒー実践対談</p>
    <div class="supervision">
      <div class="supervision-tag">監修</div>
      <div>
        <p class="supervision-role">K.B.R.T.認定コーヒーインストラクター1級</p>
        <p class="supervision-name">バリスタ森っち先生</p>
      </div>
    </div>
    <div class="portrait" role="img" aria-label="エプロン姿のバリスタ森っち先生の写真"></div>
  </section>
</main>
</body>
</html>
```